Dental Practice Billboard Design

We are a newer dental practice in need of a simple but appealing billboard for our growing dental practice to attract new patients. The practice is owned by husband and wife dentists and is family friendly in a small town in Kentucky. We try to be very friendly and caring to our patients. Would prefer a blue background for the billboard and our tooth logo to be prominent. We are partial to the Patua One font used in the image below but please feel free to tweak it as you deem necessary. The shape of the uppercase D and lowercase g are why we like that font, so fonts with a similarly shaped “D” and “g” would work as well. Please include our phone number (606) 847-3962. Please see our website Harlowfamilydentistry.com for more info on the practice if needed. Thank you! Looking forward to seeing your creation.
Updates

The dimensions will be 12ft x 24ft (3.6576m x 7.3152m). Apologies for not including this in the original prompt. Thank you all for your submissions.

Industry/Entity Type

Dental

Font styles to use
Other font styles liked:
• Patua One

Colors
0054AA
0677BA
7BADD7
CADEEF
E8F1F8
0094D4
00A9DD
6FCCEA
C7EBF8
E9F6FB
00AB8E
00BBA5
67D7C9
C6EFE9
E9F9F6
59FF00
82FF00
B8FF75
E3FFCB
F4FFEA

Requirements
Must have
• Phone number, website, Logo, Practice name “Harlow Family Dentistry”
Should not have
• A tagline or slogan

```html
<!DOCTYPE html>
<html lang="en">
<head>
<meta charset="utf-8">
<title>Harlow Family Dentistry Billboard</title>
<link rel="stylesheet" href="https://fonts.googleapis.com/css2?family=Bitter:wght@700&family=Patua+One&display=swap">
<style>
  :root {
    --backdrop: #808080;
    --brand-blue: #0457bc;
    --brand-green: #14b41a;
    --white: #ffffff;
    --photo-light: #dfe6e2;
    --photo-mid: #b9c7c1;
    --photo-dark: #6d6a6a;
  }
  * { margin: 0; padding: 0; box-sizing: border-box; }
  html, body {
    width: 1200px;
    height: 1059px;
    overflow: hidden;
    background: var(--backdrop);
  }
  .billboard {
    position: absolute;
    left: 205px;
    top: 332px;
    width: 790px;
    height: 395px;
    background: var(--brand-blue);
    overflow: hidden;
    color: var(--white);
  }
  .hours-band {
    position: absolute;
    left: 0;
    top: 340px;
    width: 580px;
    height: 55px;
    background: var(--brand-green);
  }
  .photo-shape {
    position: absolute;
    left: 0;
    top: 0;
    width: 790px;
    height: 395px;
  }
  .brand-mark {
    position: absolute;
    left: 34px;
    top: 44px;
    width: 112px;
    height: 112px;
    border-radius: 50%;
    background: var(--brand-green);
  }
  .practice-name {
    position: absolute;
    left: 162px;
    top: 46px;
    font-family: "Patua One", serif;
    line-height: 1;
  }
  .practice-name__main {
    display: block;
    font-size: 66px;
    letter-spacing: 0.5px;
  }
  .practice-name__sub {
    display: block;
    font-size: 29px;
    margin-top: 2px;
    margin-left: -6px;
  }
  .contact-row {
    position: absolute;
    left: 32px;
    display: flex;
    align-items: center;
  }
  .contact-row--phone { top: 220px; }
  .contact-row--web { top: 285px; }
  .contact-icon { flex: none; }
  .phone-number {
    font-family: "Patua One", serif;
    font-size: 42px;
    letter-spacing: 1px;
    margin-left: 10px;
    line-height: 1;
  }
  .website {
    font-family: "Bitter", serif;
    font-weight: 700;
    font-size: 21px;
    letter-spacing: 1.8px;
    margin-left: 14px;
    line-height: 1;
  }
  .office-hours {
    position: absolute;
    left: 32px;
    top: 340px;
    height: 55px;
    display: flex;
    align-items: center;
    font-family: "Bitter", serif;
    font-weight: 700;
  }
  .office-hours__label {
    color: var(--brand-blue);
    font-size: 17px;
    letter-spacing: 0.8px;
    margin-top: 10px;
  }
  .office-hours__list {
    margin-left: 10px;
    font-size: 15.5px;
    letter-spacing: 1.2px;
    line-height: 21px;
  }
</style>
</head>
<body>
  <div class="billboard">
    <div class="hours-band"></div>

    <svg class="photo-shape" viewBox="0 0 790 395" role="img" aria-label="Photo of a dentist in a white coat treating a patient in a bright clinic, framed in a tooth shape">
      <defs>
        <linearGradient id="photoTone" x1="0" y1="0" x2="1" y2="1">
          <stop offset="0" stop-color="var(--photo-light)"/>
          <stop offset="0.55" stop-color="var(--photo-mid)"/>
          <stop offset="1" stop-color="var(--photo-dark)"/>
        </linearGradient>
      </defs>
      <path fill="url(#photoTone)" d="M445 68 C430 50 440 8 475 8 C495 8 505 20 510 30 C545 25 575 40 598 56 C640 40 690 25 720 28 C718 5 760 -2 780 15 C800 35 790 65 775 75 C795 130 785 230 740 320 C720 360 700 395 660 395 L650 395 C630 380 625 360 607 345 C595 365 585 390 565 395 L540 395 C490 320 455 240 453 150 C452 110 458 90 445 68 Z"/>
    </svg>

    <div class="brand-mark"></div>
    <h1 class="practice-name">
      <span class="practice-name__main">Harlow</span>
      <span class="practice-name__sub">Family Dentistry</span>
    </h1>

    <div class="contact-row contact-row--phone">
      <svg class="contact-icon" width="34" height="34" viewBox="0 0 24 24" aria-hidden="true">
        <path fill="var(--brand-green)" d="M6.6 2.5 9.4 6.6c.4.6.3 1.3-.2 1.8L7.7 9.7c1.3 2.8 3.6 5.1 6.4 6.5l1.4-1.5c.5-.5 1.2-.6 1.8-.2l4.1 2.8c.6.4.8 1.3.3 1.9l-1.8 2.3c-.6.7-1.6 1-2.5.7C9.8 20 4 14.2 1.8 6.6c-.3-.9 0-1.9.7-2.5L4.7 2.2c.6-.5 1.5-.3 1.9.3Z"/>
        <path fill="none" stroke="var(--brand-green)" stroke-width="1.8" stroke-linecap="round" d="M13.5 6.5a4.5 4.5 0 0 1 4 4M14 2.5a8.5 8.5 0 0 1 7.5 7.5"/>
      </svg>
      <span class="phone-number">(606) 847-3962</span>
    </div>

    <div class="contact-row contact-row--web">
      <svg class="contact-icon" width="27" height="27" viewBox="0 0 24 24" aria-hidden="true">
        <g fill="none" stroke="var(--brand-green)" stroke-width="1.8">
          <circle cx="12" cy="12" r="10.5"/>
          <ellipse cx="12" cy="12" rx="4.5" ry="10.5"/>
          <path d="M1.5 12h21M3 6.5h18M3 17.5h18"/>
        </g>
      </svg>
      <span class="website">Harlowfamilydentistry.com</span>
    </div>

    <div class="office-hours">
      <span class="office-hours__label">OFFICE HOURS:-</span>
      <div class="office-hours__list">
        <div>Mon – Tue - Thu - Fri : 8AM – 5PM</div>
        <div>Sat – Sun - Wed : CLOSED</div>
      </div>
    </div>
  </div>
</body>
</html>
```